Holiday Rental Company Flyer Design (DL not A5)

Note from PixelFolk Administration: The category sizing selected is A5, however the project requires DL sized artwork. Please refer to the DL template link below while the 'Special Requirements' are updated accordingly.

Project Brief:
We need a double sided DL flyer designed for an up market Holiday Rental Company that portrays a personalised approach to property management. These are to be used for letter box drops to homes we're specifically targeting so the design should be modern, complimentary colour palette, uncluttered & visually appealing.

Please Download the DL Template from Quillmark here: http://www.quillmark.com.au/qm/ns/propath/UploadResources.aspx?selectedTab=0?pfid=BFB&pf_id=BFB&xnav=easypath-upload-image#Templates

Target Market(s)

Wealthy Home Owners

Industry/Entity Type

It Company

Font styles to use
Other font styles liked:
• Avant Garde Extra Light & Demi

Colors
33b8a4

Requirements
Must have
• DL Flyer sizes (210mm width x 99mm width, plus 3mm bleed)
• Front: Logo, Main Image & Grab
• Back: Contact Details & Brief Description of our business
• Images: Ideally the main image should be the house with the pool but alternatively a lifestyle images could also be used.
Nice to have
• A creative designer!
Should not have
• Clutter & busy designs

```html
<!DOCTYPE html>
<html lang="en">
<head>
<meta charset="utf-8">
<title>Coastline Havens – DL Flyer Front</title>
<link rel="stylesheet" href="https://fonts.googleapis.com/css2?family=Jost:wght@200;300&display=swap">
<style>
  :root {
    --teal: #2fb79e;
    --teal-deep: #27a88f;
    --ink-light: #f4fbf8;
    --glow: #c9f3e2;
    --glow-soft: rgba(214, 250, 235, 0.85);
    --photo-dark: #2a2d5a;
    --photo-light: #3f7fc4;
  }
  * { margin: 0; padding: 0; box-sizing: border-box; }
  html, body { width: 1200px; height: 580px; overflow: hidden; background: var(--teal); }
  .flyer {
    position: relative;
    width: 1200px;
    height: 580px;
    background: radial-gradient(ellipse at 40% 40%, var(--teal) 0%, var(--teal-deep) 100%);
    font-family: "Jost", "Century Gothic", sans-serif;
    color: var(--ink-light);
    overflow: hidden;
  }
  .tagline {
    position: absolute;
    top: 64px;
    left: 0;
    width: 1200px;
    padding-right: 20px;
    text-align: center;
    font-weight: 200;
    font-size: 41px;
    line-height: 50px;
    letter-spacing: 1.5px;
    text-transform: uppercase;
    white-space: nowrap;
  }
  .brand {
    position: absolute;
    left: 40px;
    top: 238px;
    width: 480px;
    text-align: center;
  }
  .brand-name {
    font-weight: 200;
    font-size: 62px;
    line-height: 74px;
    letter-spacing: 8px;
    text-transform: uppercase;
    white-space: nowrap;
  }
  .brand-mark {
    display: block;
    margin: 8px auto 0;
  }
  .hero-frame {
    position: absolute;
    left: 540px;
    top: 163px;
    width: 636px;
    height: 397px;
    border-radius: 90px / 70px;
    background: var(--glow);
    box-shadow: 0 0 18px 6px var(--glow-soft), inset 0 0 16px 4px rgba(47, 183, 158, 0.45);
  }
  .hero-photo {
    position: absolute;
    left: 20px;
    top: 20px;
    right: 18px;
    bottom: 20px;
    border-radius: 74px / 56px;
    background: linear-gradient(160deg, var(--photo-dark) 0%, var(--photo-light) 100%);
    box-shadow: 0 0 10px 3px rgba(230, 255, 245, 0.9);
  }
</style>
</head>
<body>
  <main class="flyer">
    <h1 class="tagline">Holiday rental management with a difference</h1>

    <div class="brand">
      <p class="brand-name">Coastline<br>Havens</p>
      <svg class="brand-mark" width="90" height="90" viewBox="0 0 90 90" aria-hidden="true">
        <circle cx="45" cy="45" r="38" fill="none" stroke="var(--ink-light)" stroke-width="2"/>
      </svg>
    </div>

    <div class="hero-frame">
      <div class="hero-photo" role="img" aria-label="Photograph of a modern luxury holiday home at dusk beside a lit swimming pool"></div>
    </div>
  </main>
</body>
</html>
```